Wordpress Design Project

Hello, my name is Dermot Vasey and I am a Professor at a university in Hong Kong. I am looking for a clean and professional website to introduce myself with my bio, resume, and contact info. Looking for a creative & professional personal website, because all the information is very textual and I am looking forward to see how you can make it look good.
Updates
Project Deadline Extended
Reason: Can't find a satisfying design so far. Looking forward to see better ones.
I have added a zip file call "Good Examples" please look at the screenshot I attach. These are the quality that I am looking forward to see in your work.
Project Deadline Extended
Reason: It looks like we need more time
Project Deadline Extended
Reason: Need more time, waiting for designs
Target Market(s)
Potential Business Clients & Partners
Industry/Entity Type
University
Requirements
Must have
- The Design:
Please include photos of the schools I went to, e.g. Pellham College in Michigan, read my resume for more. You can also download the logos of the organization or institute and include them in my website to make the website more professional, just make sure the logo you found on google is correct.
The Development:
The final deliverable must be a fully coded, functional website. Site must be tested and good to go in IE 7+, Firefox 9+, Chrome and both Apple and Android Mobile platforms. Blog must be one that church can easily upload content to as an integrated part of the site (no Jotlane.com, etc plugins please).
Final handover must include full rights to the designs, stock art, coding, etc (so, no "one use templates" please).
Final handover will include loading and testing on to our hosting server.
The designer must be willing to support the site for 30 days after launch as part of the site payment.
Nice to have
- I have attached some scanned photos of myself. They are really blurry and low quality, can you do some touch ups in photoshop? Because I would still love to have the photos appear somewhere in the website (e.g. inside a banner).
You can also find my photos on google by searching my name "Dermot Vasey", just make sure you find the right one.
Should not have
- Anything that looks cheap and amateurish, no flash. Anything that looks like a cookie cutter website.

```html
<!DOCTYPE html>
<html lang="en">
<head>
<meta charset="utf-8">
<title>Dermot Vasey</title>
<link href="https://fonts.googleapis.com/css2?family=Kreon:wght@400;700&family=Ubuntu:wght@500&family=Open+Sans:wght@400;600&display=swap" rel="stylesheet">
<style>
:root{
  --blue:#0a76c4;
  --blue-bright:#2a9ee8;
  --blue-deep:#1672c0;
  --grey-logo:#a9a9a9;
  --ink:#333;
  --text:#444;
  --dark:#2b2b2b;
  --darker:#1d1d1d;
  --footer-bar:#4b4b4b;
  --white:#fff;
}
*{margin:0;padding:0;box-sizing:border-box}
html,body{width:1200px;height:1180px;overflow:hidden}
body{position:relative;background:#f7f7f7;font-family:Arial,Helvetica,sans-serif;color:var(--text)}
.abs{position:absolute}

.site-header{position:absolute;left:0;top:0;width:1200px;height:116px;background:linear-gradient(#3d3d3d,#1e1e1e)}
.brand{left:112px;top:26px;font-family:'Kreon',serif;font-weight:700;font-size:48px;letter-spacing:.5px}
.brand .first{color:var(--blue-bright)}
.brand .last{color:var(--grey-logo)}
.phone{left:885px;top:9px;display:flex;align-items:center;gap:10px;font-family:'Open Sans',sans-serif;font-weight:600;font-size:24px;color:#9c9c9c;letter-spacing:1px}
.phone-icon{width:26px;height:26px;border-radius:4px;background:linear-gradient(#3aa6ee,#0f6db8);display:flex;align-items:center;justify-content:center}

.main-nav{position:absolute;left:0;top:116px;width:1200px;height:44px;background:linear-gradient(#49b1f4,#1f8ee0 55%,#177ccc)}
.nav-item{position:absolute;top:0;height:44px;line-height:44px;color:var(--white);font-size:15px;text-transform:uppercase}
.nav-item.active{top:4px;height:35px;line-height:35px;padding:0 17px;background:linear-gradient(#4a4a4a,#1f1f1f);border-radius:6px;box-shadow:0 0 0 1px #6fb9ec}
.nav-sep{position:absolute;top:8px;width:1px;height:28px;background:#0f5f9e;box-shadow:1px 0 0 #64bdf5}
.search{left:883px;top:7px;width:212px;height:28px;border-radius:14px;background:#0d5996;box-shadow:inset 0 1px 3px rgba(0,0,0,.4)}

.hero-photo{position:absolute;background:#fff;padding:3px;box-shadow:0 1px 6px rgba(0,0,0,.25)}
.hero-photo div{width:100%;height:100%}
.arrow{position:absolute;top:320px;width:52px;height:52px;border-radius:50%;background:radial-gradient(#fafafa,#cfcfcf);border:3px solid #8a8a8a}
.hero-title{left:664px;top:218px;width:420px;font-family:'Kreon',serif;font-weight:700;font-size:26px;line-height:30px;color:var(--blue)}
.hero-title .dark{color:var(--ink)}
.hero-text{left:673px;top:326px;width:412px;font-size:14px;line-height:20px;color:#333;text-align:justify}
.hero-text p{margin-bottom:20px}
.btn-bio{left:666px;top:456px;width:207px;height:38px;border-radius:10px;background:linear-gradient(#3aa8f0,#1470bf);color:#fff;font-family:'Ubuntu',sans-serif;font-weight:500;font-size:15px;text-align:center;line-height:38px;letter-spacing:.5px}
.divider{left:110px;top:538px;width:980px;height:8px;background:radial-gradient(ellipse at center top,rgba(0,0,0,.22),transparent 70%)}

.card{position:absolute;top:573px;width:236px;height:254px;border-left:1px dotted #999}
.card-photo{position:absolute;left:8px;top:6px;width:213px;height:120px;background:#fff;border:1px solid #ddd;padding:6px}
.card-photo div{width:100%;height:100%}
.card h3{position:absolute;left:16px;top:130px;font-family:'Ubuntu',sans-serif;font-weight:500;font-size:18px;color:#3a3a3a}
.card p{position:absolute;left:16px;top:158px;width:195px;font-size:12px;line-height:18px;text-align:justify;color:#444}
.more{position:absolute;right:14px;top:224px;display:flex;align-items:center;gap:4px;font-family:'Open Sans',sans-serif;font-size:12px;color:#444}
.plus{width:22px;height:22px;border-radius:50%;background:linear-gradient(#5ab9f5,#1478c8);color:#fff;font-weight:700;text-align:center;line-height:22px;font-size:18px}

.site-footer{position:absolute;left:0;top:870px;width:1200px;height:249px;background:var(--dark)}
.foot-col h4{position:absolute;top:14px;font-family:'Open Sans',sans-serif;font-weight:400;font-size:20px;color:#fff}
.foot-col h4 b{font-weight:600}
.foot-rule{position:absolute;top:20px;width:2px;height:200px;background:#ddd}
.social{position:absolute;left:112px;display:flex;align-items:center;gap:8px;font-family:'Open Sans',sans-serif;font-weight:600;font-size:22px;color:#e8e8e8}
.social i{display:block;width:36px;height:36px;border-radius:4px}
.post{left:346px;top:54px;width:240px;font-size:12px;line-height:24px;color:#eee;letter-spacing:.3px}
.archives{left:638px;top:58px;list-style:none;font-size:12px;line-height:24px;color:#eee;letter-spacing:.5px}
.archives li::before{content:"";display:inline-block;border-left:4px solid #ddd;border-top:3px solid transparent;border-bottom:3px solid transparent;margin-right:8px}
.field{position:absolute;left:830px;width:212px;height:28px;border-radius:14px;border:2px solid #8b8b8b;background:#333;color:#eee;font-size:12px;padding:6px 10px}
.copyright{position:absolute;left:0;top:1119px;width:1200px;height:61px;background:var(--footer-bar);color:#fff;font-size:12px;text-align:center;line-height:74px;letter-spacing:.3px}
</style>
</head>
<body>
<header class="site-header">
  <div class="abs brand"><span class="first">Dermot</span> <span class="last">Vasey</span></div>
  <div class="abs phone"><span class="phone-icon"><svg width="14" height="16" viewBox="0 0 14 16"><path d="M3 1l3 3-2 2c1 2 2 4 4 5l2-2 3 3-2 3C5 14 1 9 1 3z" fill="#fff"/></svg></span>(555) 204 7719</div>
</header>

<nav class="main-nav">
  <span class="nav-item active" style="left:110px">Home</span>
  <span class="nav-sep" style="left:198px"></span>
  <span class="nav-item" style="left:230px">About Us</span>
  <span class="nav-sep" style="left:334px"></span>
  <span class="nav-item" style="left:363px">Bio</span>
  <span class="nav-sep" style="left:419px"></span>
  <span class="nav-item" style="left:448px">Resume</span>
  <span class="nav-sep" style="left:538px"></span>
  <span class="nav-item" style="left:569px">Contact Us</span>
  <span class="nav-sep" style="left:692px"></span>
  <div class="abs search"><svg class="abs" style="left:180px;top:4px" width="22" height="20" viewBox="0 0 22 20"><circle cx="8" cy="8" r="6" fill="none" stroke="#fff" stroke-width="2.4"/><path d="M12 12l7 6" stroke="#fff" stroke-width="3.5" stroke-linecap="round"/></svg></div>
</nav>

<section class="hero">
  <span class="arrow" style="left:65px"><svg class="abs" style="left:12px;top:14px" width="20" height="20"><path d="M16 2L4 10l12 8z" fill="#555"/></svg></span>
  <span class="arrow" style="left:584px"><svg class="abs" style="left:16px;top:14px" width="20" height="20"><path d="M4 2l12 8-12 8z" fill="#555"/></svg></span>
  <div class="hero-photo" style="left:103px;top:232px;width:120px;height:246px"><div role="img" aria-label="Award ceremony photo" style="background:linear-gradient(#d8c24a,#b89a40 40%,#c8c0b0)"></div></div>
  <div class="hero-photo" style="left:472px;top:232px;width:123px;height:246px"><div role="img" aria-label="Award presentation on stage" style="background:linear-gradient(#2a4a70,#6ea060 50%,#7a6a58)"></div></div>
  <div class="hero-photo" style="left:214px;top:189px;width:262px;height:312px"><div role="img" aria-label="Professor receiving an award" style="background:linear-gradient(#c89a50,#b07a40 45%,#c05040)"></div></div>
  <h1 class="abs hero-title">Dermot Vasey <span class="dark">(BA, MA, PhD)</span> is a Professor in the Department of Management at Hong Kong</h1>
  <div class="abs hero-text">
    <p><b>He is a certified Senior Professional in Human Resources as well as a registered Industrial-Organizational</b></p>
    <p>Psychologist and holds six other professional qualifications. Before he began his career in teaching and management consulting,</p>
  </div>
  <div class="abs btn-bio">MYSELF WITH MY BIO</div>
  <div class="abs divider"></div>
</section>

<section class="features">
  <article class="card" style="left:120px"><div class="card-photo"><div role="img" aria-label="Group photo at an award event" style="background:linear-gradient(#d8e4f0,#8a8a8a)"></div></div><h3>About Dermot Vasey</h3><p>Dermot Vasey (BA, MA, PhD) is a Professor in the Department of Management at Hong Kong ...</p><span class="more">View More <span class="plus">+</span></span></article>
  <article class="card" style="left:361px"><div class="card-photo"><div role="img" aria-label="Seminar handshake photo" style="background:linear-gradient(#d0e6d0,#909090)"></div></div><h3>Career History</h3><p>Dermot Vasey (BA, MA, PhD) is a Professor in the Department of Management at Hong Kong ...</p><span class="more">View More <span class="plus">+</span></span></article>
  <article class="card" style="left:604px"><div class="card-photo"><div role="img" aria-label="Speech at an annual dinner" style="background:linear-gradient(#e8e8e8,#5a5a5a)"></div></div><h3>Educational Achiev</h3><p>Dermot Vasey (BA, MA, PhD) is a Professor in the Department of Management at Hong Kong ...</p><span class="more">View More <span class="plus">+</span></span></article>
  <article class="card" style="left:840px;border-right:1px dotted #999;width:240px"><div class="card-photo"><div role="img" aria-label="Summit award photo" style="background:linear-gradient(90deg,#c8302a,#d86030 60%,#e89030)"></div></div><h3>Memberships</h3><p>Dermot Vasey (BA, MA, PhD) is a Professor in the Department of Management at Hong Kong ...</p><span class="more">View More <span class="plus">+</span></span></article>
</section>

<footer class="site-footer">
  <div class="foot-col"><h4 style="left:108px">Social <b>Media</b></h4>
    <div class="social" style="top:58px"><i style="background:#3b5a9a"></i>Circlebook</div>
    <div class="social" style="top:120px"><i style="background:#35a8e0"></i>Chirpline</div>
    <div class="social" style="top:186px"><i style="background:#0e6aa8"></i>Workfolio</div>
  </div>
  <span class="foot-rule" style="left:312px"></span>
  <div class="foot-col"><h4 style="left:348px">Recent <b>Post</b></h4>
    <div class="abs post"><p>Lorem Ipsum is simply dummy text of the printing and typesetting industry. Lorem Ipsum has</p><p style="margin-top:24px">Nasaece ristique orci ferode fereaseras Mirum est notare quam littera</p></div>
  </div>
  <span class="foot-rule" style="left:603px"></span>
  <div class="foot-col"><h4 style="left:638px"><b>Archives</b></h4>
    <ul class="abs archives"><li>May 2011</li><li>April 2011</li><li>March 2011</li><li>February 2011</li><li>January 2011</li></ul>
  </div>
  <span class="foot-rule" style="left:806px"></span>
  <div class="foot-col"><h4 style="left:837px">Leave your <b>Message</b></h4>
    <div class="field" style="top:60px">----Name----</div>
    <div class="field" style="top:98px">----Email----</div>
    <div class="field" style="top:137px;height:67px;width:214px;border-radius:12px">---- Your Message ------</div>
  </div>
</footer>
<div class="copyright">Copyright © 2011-12 dermotvasey.com.au</div>
</body>
</html>
```